Fun Location App for users to earn rewards and vouchers everywhere they go

Tovrim is a social app where users can collect rewards when they travel + complete quests at different location to get rewards.

We would like a design of an app that has these features/function
1) Login/Signup Page
2) HomePage - A Map with your current location
- Show the location/stores aroudn
- Have a bag tab to press and get rewards
3) Quests Tab = show all the available tasks
4) Exchange Tab = all the items available for exchange vouchers and can click to know more
5) Wallet Tab = user profile + vouchers in their wallet
6) Partners Tab = Showcase all the partners and can click to know more
7) Claim functions

We have attached a visual example. Do feel free to change what is best fit too. We do need to exact measurements as well to create the app

Target Market(s)

Fun, people who like rewards and interact with friends

Font styles to use
Sans Serif

Colors
f78f20
fbed22
fbee3e

Requirements
Must have
• Yellow, fun interactive feeling.
Nice to have
• Pop up when click on things
Should not have
• nil

```html
<!DOCTYPE html>
<html lang="en">
<head>
<meta charset="utf-8">
<title>Tovrim – App Screens</title>
<link rel="stylesheet" href="https://fonts.googleapis.com/css2?family=Nunito+Sans:wght@400;600;700;800&display=swap">
<style>
:root{
  --orange:#f78f20;
  --yellow:#fbed22;
  --yellow-soft:#fbee3e;
  --amber:#f9a825;
  --bg:#eef0f3;
  --screen:#f7f7f8;
  --ink:#3d3d42;
  --ink-soft:#8a8a92;
  --dark-bar:#3b3b3f;
  --line:#d9dadf;
  --pink:#f0365a;
}
*{box-sizing:border-box;margin:0;padding:0}
html,body{width:1200px;height:2290px;overflow:hidden}
body{background:var(--bg);font-family:"Nunito Sans",Arial,sans-serif;color:var(--ink);position:relative}
.screen{position:absolute;width:270px;height:560px;border-radius:34px;background:var(--screen);overflow:hidden;box-shadow:0 20px 40px rgba(120,125,140,.18),0 2px 6px rgba(120,125,140,.12)}
.abs{position:absolute}
.center{left:0;right:0;text-align:center}

.brand{position:absolute;left:0;right:0;display:flex;align-items:center;justify-content:center;gap:8px;font-weight:800;color:var(--ink)}
.brand .dot{width:18px;height:18px;border-radius:50%;background:var(--yellow)}

.btn{position:absolute;height:32px;border-radius:16px;font-size:11px;font-weight:700;display:flex;align-items:center;justify-content:center}
.btn-primary{background:linear-gradient(90deg,var(--orange),var(--amber));color:#fff;box-shadow:0 6px 12px rgba(247,143,32,.3)}
.btn-ghost{background:#fafafa;color:var(--ink);box-shadow:0 4px 10px rgba(0,0,0,.07)}
.footer-note{position:absolute;left:0;right:0;bottom:18px;text-align:center;font-size:6.5px;color:#a8a8b0;font-weight:600}

.field{position:absolute;left:38px;width:194px;height:40px;border:1px solid var(--line);border-radius:4px}
.field span{position:absolute;top:-6px;left:20px;background:var(--screen);padding:0 6px;font-size:7.5px;font-weight:700}

.header{position:absolute;left:16px;right:16px;top:14px;border-radius:0 0 30px 30px;background:linear-gradient(160deg,var(--orange),var(--amber) 60%,#fbc12a);color:#fff;text-align:center}
.header h2{font-size:14px;font-weight:800}
.header p{font-size:9.5px;opacity:.9}
.avatar{position:absolute;width:28px;height:28px;border-radius:50%;background:linear-gradient(135deg,#9fb6d6,#d8a77f);border:2px solid #fff}
.back{position:absolute;width:22px;height:14px}

.item{position:absolute;left:22px;right:22px;height:56px}
.thumb{position:absolute;left:0;top:0;width:88px;height:50px;border-radius:2px}
.t1{background:linear-gradient(135deg,#3a2419,#8c4a2a 60%,#2b1c16)}
.t2{background:linear-gradient(135deg,#5d8fb8,#b886a6 55%,#3c5a7e)}
.t3{background:linear-gradient(135deg,#2a1f5c,#7c56d9 55%,#151022)}
.t4{background:linear-gradient(135deg,#1f3346,#6b4f4a 55%,#1a2532)}
.t5{background:linear-gradient(135deg,#1b1445,#c03fa0 50%,#2c2070)}
.t6{background:linear-gradient(135deg,#cfcbbb,#8e9a74 55%,#e8e3d2)}
.t7{background:linear-gradient(135deg,#40505a,#8b9e8e 55%,#2d3a41)}
.item h4{position:absolute;left:98px;top:6px;font-size:9.5px;font-weight:700}
.item p{position:absolute;left:98px;top:21px;font-size:9px;color:var(--ink-soft)}
.item .pts{position:absolute;left:98px;top:38px;font-size:6.5px;font-weight:800}
.bar{position:absolute;left:98px;top:48px;width:66px;height:2px;background:#e4e4e8;border-radius:2px}
.bar i{display:block;height:100%;background:var(--pink);border-radius:2px}
.act{position:absolute;right:0;top:9px;width:32px;height:32px;border-radius:50%;display:flex;align-items:center;justify-content:center;box-shadow:0 5px 10px rgba(0,0,0,.15)}
.act.dark{background:var(--dark-bar)}
.act.gold{background:linear-gradient(135deg,var(--amber),var(--yellow-soft))}
.act svg{width:13px;height:13px}
.fade{opacity:.25}

.tabbar{position:absolute;left:12px;right:12px;bottom:12px;height:48px;border-radius:22px;background:linear-gradient(180deg,#4a4a4f,var(--dark-bar));display:flex;justify-content:space-around;align-items:flex-end;padding:0 6px 8px}
.tab{width:44px;text-align:center;color:#eee;font-size:7px;font-weight:600}
.tab svg{display:block;width:14px;height:14px;margin:0 auto 4px}
.tab.on{color:var(--amber)}
.tab.mid{position:relative}
.tab.mid .bubble{position:absolute;left:8px;top:-30px;width:28px;height:28px;border-radius:50%;background:linear-gradient(135deg,var(--orange),var(--yellow-soft));display:flex;align-items:center;justify-content:center;box-shadow:0 0 0 4px var(--dark-bar)}
.tab.mid .bubble svg{margin:0;width:12px;height:12px}
.map{position:absolute;inset:0;background:radial-gradient(circle at 50% 55%,#d9d3c4,#cdc8ba 50%,#8c8a84)}
.toggle{position:absolute;width:28px;height:28px;border-radius:50%;display:flex;align-items:center;justify-content:center}
</style>
</head>
<body>

<!-- Splash -->
<section class="screen" style="left:100px;top:80px">
  <div class="brand" style="top:220px;font-size:24px"><span class="dot"></span>Tovrim</div>
  <div class="btn btn-primary" style="left:64px;width:142px;top:362px">Login</div>
  <div class="btn btn-ghost" style="left:64px;width:142px;top:430px">Create an Account</div>
  <div class="footer-note">Powered by Lumen Protocol</div>
</section>

<!-- Login -->
<section class="screen" style="left:465px;top:50px">
  <svg class="back" style="left:32px;top:52px" viewBox="0 0 22 14"><path d="M21 7H2M7 1L1 7l6 6" fill="none" stroke="#3d3d42" stroke-width="1.5"/></svg>
  <div class="brand" style="top:140px;font-size:22px"><span class="dot"></span>Tovrim</div>
  <div class="abs" style="left:52px;top:212px;font-size:14px;font-weight:800;color:#9b9ba3">Welcome Back!</div>
  <div class="abs" style="left:52px;top:232px;font-size:9px;font-weight:700">Lena</div>
  <div class="field" style="top:270px"><span>Mobile No.</span></div>
  <div class="field" style="top:330px"><span>OTP Code</span></div>
  <div class="btn btn-ghost" style="left:52px;width:74px;top:397px;font-size:7.5px">Resend Code</div>
  <div class="btn btn-primary" style="left:148px;width:74px;top:397px">Login</div>
  <div class="abs center" style="top:470px;font-size:6.5px;font-weight:700;line-height:1.6">By login you have agree to Terms of use and<br>Privacy Plicy on Tovrim Pte. Ltd.</div>
  <div class="footer-note" style="bottom:30px">Powered by Lumen Protocol</div>
</section>

<!-- Map / Home -->
<section class="screen" style="left:830px;top:100px">
  <div class="map" role="img" aria-label="Street map of the surrounding neighbourhood with nearby store pins"></div>
  <svg class="back" style="left:20px;top:46px" viewBox="0 0 22 14"><path d="M21 7H2M7 1L1 7l6 6" fill="none" stroke="#3d3d42" stroke-width="1.5"/></svg>
  <div class="avatar" style="left:220px;top:38px" role="img" aria-label="User profile photo"></div>
  <div class="abs" style="left:22px;top:102px;width:206px;height:48px;border-radius:8px;background:linear-gradient(90deg,#3a3c4a,#59595f);color:#fff;padding:6px 12px">
    <div style="font-family:Georgia,serif;font-size:11px;letter-spacing:.5px">LIFE an ADVENTURE</div>
    <div style="font-size:7.5px;font-weight:800;color:var(--yellow)">10% OFF THIS SEASON</div>
    <div style="font-size:6.5px;font-weight:700">visit: www.dealpocket.test</div>
    <div class="abs" style="right:10px;top:24px;width:46px;height:12px;border-radius:6px;background:var(--yellow);color:var(--ink);font-size:6.5px;font-weight:800;text-align:center;line-height:12px">FREE</div>
  </div>
  <div class="abs" style="left:214px;top:94px;width:18px;height:18px;border-radius:50%;background:var(--pink);color:#fff;font-size:11px;text-align:center;line-height:17px">×</div>
  <div class="abs" style="left:92px;top:224px;width:86px;height:86px;border-radius:50%;border:1px dashed rgba(80,80,80,.45)"></div>
  <div class="abs" style="left:111px;top:243px;width:48px;height:48px;border-radius:50%;background:rgba(110,110,110,.45)"></div>
  <svg class="abs" style="left:124px;top:252px;width:22px;height:28px" viewBox="0 0 22 28"><path d="M11 27C4 18 1 14 1 10a10 10 0 0 1 20 0c0 4-3 8-10 17z" fill="#fbc12a"/><circle cx="11" cy="10" r="4" fill="#fff"/></svg>
  <div class="abs" style="left:192px;top:420px;width:36px;height:36px;border-radius:50%;background:var(--dark-bar);display:flex;align-items:center;justify-content:center">
    <svg width="18" height="18" viewBox="0 0 18 18"><circle cx="9" cy="9" r="6" fill="none" stroke="#fff" stroke-width="1.3"/><path d="M9 1v4M9 13v4M1 9h4M13 9h4" stroke="#fff" stroke-width="1.3"/></svg>
  </div>
  <nav class="tabbar">
    <div class="tab"><svg viewBox="0 0 14 14"><path d="M2 7L7 2l5 5v6H2z" fill="none" stroke="currentColor" stroke-width="1.2"/></svg>Home</div>
    <div class="tab"><svg viewBox="0 0 14 14"><path d="M1 5h12M1 9h12M10 2l3 3M4 12L1 9" fill="none" stroke="currentColor" stroke-width="1.2"/></svg>Exchange</div>
    <div class="tab mid on"><span class="bubble"><svg viewBox="0 0 14 14"><circle cx="7" cy="7" r="5" fill="none" stroke="#fff" stroke-width="1.4"/></svg></span>Quests</div>
    <div class="tab"><svg viewBox="0 0 14 14"><circle cx="5" cy="5" r="2.5" fill="none" stroke="currentColor" stroke-width="1.2"/><path d="M1 13c0-3 2-5 4-5s4 2 4 5M9 3a2 2 0 0 1 0 4M11 9c1 1 2 2 2 4" fill="none" stroke="currentColor" stroke-width="1.2"/></svg>Partners</div>
    <div class="tab"><svg viewBox="0 0 14 14"><rect x="1" y="3" width="12" height="9" rx="2" fill="none" stroke="currentColor" stroke-width="1.2"/><path d="M9 7h4" stroke="currentColor" stroke-width="1.2"/></svg>Wallet</div>
  </nav>
</section>

<!-- Wallet -->
<section class="screen" style="left:100px;top:860px">
  <header class="header" style="height:134px;padding-top:56px">
    <h2>Rafe Okoli</h2>
    <p>@rafeokoli</p>
    <p>55,000 tovcoins</p>
    <p style="font-weight:700">Referral code <b>ebD3Q</b></p>
  </header>
  <svg class="back" style="left:30px;top:52px" viewBox="0 0 22 14"><path d="M21 7H2M7 1L1 7l6 6" fill="none" stroke="#fff" stroke-width="1.5"/></svg>
  <div class="avatar" style="left:208px;top:40px" role="img" aria-label="User profile photo"></div>
  <div class="abs" style="left:16px;right:16px;top:148px;height:100px;border-radius:0 0 28px 28px;background:#fafafa;box-shadow:0 8px 14px rgba(0,0,0,.06)">
    <div class="abs center" style="top:10px;font-size:12px;font-weight:800">+65 5550 1234</div>
    <div class="abs center" style="top:28px;font-size:9px;color:var(--ink-soft)">rafe@mailbox.test</div>
    <div class="abs" style="right:18px;top:10px;width:22px;height:22px;border-radius:50%;background:#e6e6ea"></div>
    <div class="abs" style="left:48px;top:70px;font-size:9px;font-weight:700;color:var(--amber);border-bottom:2px solid var(--amber);padding:0 6px 3px">Vouchers</div>
    <div class="abs" style="left:118px;top:64px;width:1px;height:22px;background:var(--line)"></div>
    <div class="abs" style="left:152px;top:70px;font-size:9px;font-weight:700">Swarm</div>
  </div>
  <div class="item" style="top:268px"><div class="thumb t1" role="img" aria-label="Bricklane restaurant interior photo"></div><h4>Bricklane</h4><p>$1 off any item</p><div class="act gold"><svg viewBox="0 0 13 13"><path d="M1 6.5h10M7 2l4.5 4.5L7 11" fill="none" stroke="#fff" stroke-width="1.5"/></svg></div></div>
  <div class="item" style="top:332px"><div class="thumb t2" role="img" aria-label="Sakane bar evening photo"></div><h4>Sakane bar</h4><p>$1 off any item</p><div class="act dark"><svg viewBox="0 0 13 13"><path d="M2 7l3 3 6-6" fill="none" stroke="#fff" stroke-width="1.5"/></svg></div></div>
  <div class="item" style="top:396px"><div class="thumb t3" role="img" aria-label="Auckland concert crowd photo"></div><h4>Auckland</h4><p>$1 off any item</p><div class="act dark"><svg viewBox="0 0 13 13"><path d="M2 7l3 3 6-6" fill="none" stroke="#fff" stroke-width="1.5"/></svg></div></div>
  <div class="abs" style="left:108px;top:458px;width:54px;height:14px;border:1px solid var(--line);border-radius:7px;font-size:6.5px;text-align:center;line-height:12px;color:var(--ink-soft)">Load more</div>
  <nav class="tabbar">
    <div class="tab on"><svg viewBox="0 0 14 14"><path d="M2 7L7 2l5 5v6H2z" fill="none" stroke="currentColor" stroke-width="1.2"/></svg>Home</div>
    <div class="tab"><svg viewBox="0 0 14 14"><path d="M1 5h12M1 9h12M10 2l3 3M4 12L1 9" fill="none" stroke="currentColor" stroke-width="1.2"/></svg>Exchange</div>
    <div class="tab mid"><span class="bubble"><svg viewBox="0 0 14 14"><circle cx="7" cy="7" r="5" fill="none" stroke="#fff" stroke-width="1.4"/></svg></span>Quests</div>
    <div class="tab"><svg viewBox="0 0 14 14"><circle cx="5" cy="5" r="2.5" fill="none" stroke="currentColor" stroke-width="1.2"/><path d="M1 13c0-3 2-5 4-5s4 2 4 5M9 3a2 2 0 0 1 0 4M11 9c1 1 2 2 2 4" fill="none" stroke="currentColor" stroke-width="1.2"/></svg>Partners</div>
    <div class="tab"><svg viewBox="0 0 14 14"><rect x="1" y="3" width="12" height="9" rx="2" fill="none" stroke="currentColor" stroke-width="1.2"/><path d="M9 7h4" stroke="currentColor" stroke-width="1.2"/></svg>Wallet</div>
  </nav>
</section>

<!-- Quests -->
<section class="screen" style="left:465px;top:830px">
  <header class="header" style="height:104px;padding-top:50px">
    <h2>Quest Time!</h2>
    <p>Challanage to earn rewards</p>
  </header>
  <div class="avatar" style="left:208px;top:36px" role="img" aria-label="User profile photo"></div>
  <div class="item" style="top:132px"><div class="thumb t1" role="img" aria-label="Bricklane restaurant interior photo"></div><h4>Bricklane</h4><p>$1 off any item</p><div class="act dark"><svg viewBox="0 0 13 13"><path d="M1 6.5h10M7 2l4.5 4.5L7 11" fill="none" stroke="#fff" stroke-width="1.5"/></svg></div></div>
  <div class="item" style="top:197px"><div class="thumb t2" role="img" aria-label="Sakane bar evening photo"></div><h4>Sakane bar</h4><p>$1 off any item</p><div class="act gold"><svg viewBox="0 0 13 13"><path d="M2 7l3 3 6-6" fill="none" stroke="#fff" stroke-width="1.5"/></svg></div></div>
  <div class="item" style="top:262px"><div class="thumb t3" role="img" aria-label="Auckland concert crowd photo"></div><h4>Auckland</h4><p>$1 off any item</p><div class="act dark"><svg viewBox="0 0 13 13"><path d="M1 6.5h10M7 2l4.5 4.5L7 11" fill="none" stroke="#fff" stroke-width="1.5"/></svg></div></div>
  <div class="item" style="top:327px"><div class="thumb t4" role="img" aria-label="The Hague night scene photo"></div><h4>The Hague</h4><p>$1 off any item</p><div class="act gold"><svg viewBox="0 0 13 13"><path d="M2 7l3 3 6-6" fill="none" stroke="#fff" stroke-width="1.5"/></svg></div></div>
  <div class="item" style="top:392px"><div class="thumb t5" role="img" aria-label="Halifax festival lights photo"></div><h4>Halifax</h4><p>$1 off any item</p><div class="act gold"><svg viewBox="0 0 13 13"><path d="M2 7l3 3 6-6" fill="none" stroke="#fff" stroke-width="1.5"/></svg></div></div>
  <div class="item fade" style="top:457px"><div class="thumb t3" role="img" aria-label="Next quest location photo"></div><h4>Halifax</h4></div>
  <nav class="tabbar">
    <div class="tab"><svg viewBox="0 0 14 14"><path d="M2 7L7 2l5 5v6H2z" fill="none" stroke="currentColor" stroke-width="1.2"/></svg>Home</div>
    <div class="tab"><svg viewBox="0 0 14 14"><path d="M1 5h12M1 9h12M10 2l3 3M4 12L1 9" fill="none" stroke="currentColor" stroke-width="1.2"/></svg>Exchange</div>
    <div class="tab mid on"><span class="bubble"><svg viewBox="0 0 14 14"><circle cx="7" cy="7" r="5" fill="none" stroke="#fff" stroke-width="1.4"/></svg></span>Quests</div>
    <div class="tab"><svg viewBox="0 0 14 14"><circle cx="5" cy="5" r="2.5" fill="none" stroke="currentColor" stroke-width="1.2"/><path d="M1 13c0-3 2-5 4-5s4 2 4 5M9 3a2 2 0 0 1 0 4M11 9c1 1 2 2 2 4" fill="none" stroke="currentColor" stroke-width="1.2"/></svg>Partners</div>
    <div class="tab"><svg viewBox="0 0 14 14"><rect x="1" y="3" width="12" height="9" rx="2" fill="none" stroke="currentColor" stroke-width="1.2"/><path d="M9 7h4" stroke="currentColor" stroke-width="1.2"/></svg>Wallet</div>
  </nav>
</section>

<!-- Exchange -->
<section class="screen" style="left:830px;top:880px">
  <header class="header" style="height:104px;padding-top:50px">
    <h2>Trade Street</h2>
    <p>55,000 tovcoins</p>
  </header>
  <div class="avatar" style="left:208px;top:36px" role="img" aria-label="User profile photo"></div>
  <div class="item" style="top:128px"><div class="thumb t1" role="img" aria-label="Bricklane restaurant interior photo"></div><h4>Bricklane</h4><p>$1 off any food</p><span class="pts">4000 tovcoins</span><span class="bar"><i style="width:40%"></i></span><div class="act dark"><svg viewBox="0 0 13 13"><path d="M1 6.5h10M7 2l4.5 4.5L7 11" fill="none" stroke="#fff" stroke-width="1.5"/></svg></div></div>
  <div class="item" style="top:193px"><div class="thumb t2" role="img" aria-label="Riverside evening photo"></div><h4>Riverside</h4><p>$1 off any food</p><span class="pts">7000 tovcoins</span><span class="bar"><i style="width:70%"></i></span><div class="act gold"><svg viewBox="0 0 13 13"><path d="M2 7l3 3 6-6" fill="none" stroke="#fff" stroke-width="1.5"/></svg></div></div>
  <div class="item" style="top:258px"><div class="thumb t3" role="img" aria-label="Bridgetown concert crowd photo"></div><h4>Bridgetown</h4><p>$1 off any food</p><span class="pts">3000 tovcoins</span><span class="bar"><i style="width:30%"></i></span><div class="act dark"><svg viewBox="0 0 13 13"><path d="M1 6.5h10M7 2l4.5 4.5L7 11" fill="none" stroke="#fff" stroke-width="1.5"/></svg></div></div>
  <div class="item" style="top:323px"><div class="thumb t6" role="img" aria-label="Astana outdoor cafe photo"></div><h4>Astana</h4><p>$1 off any food</p><span class="pts">1000 tovcoins</span><span class="bar"><i style="width:20%"></i></span><div class="act gold"><svg viewBox="0 0 13 13"><path d="M2 7l3 3 6-6" fill="none" stroke="#fff" stroke-width="1.5"/></svg></div></div>
  <div class="item" style="top:388px"><div class="thumb t7" role="img" aria-label="Stuttgart shopfront photo"></div><h4>Stuttgart</h4><p>$1 off any food</p><span class="pts">4000 tovcoins</span><span class="bar"><i style="width:40%"></i></span><div class="act gold"><svg viewBox="0 0 13 13"><path d="M2 7l3 3 6-6" fill="none" stroke="#fff" stroke-width="1.5"/></svg></div></div>
  <div class="item fade" style="top:453px"><div class="thumb t3" role="img" aria-label="Next partner location photo"></div><h4>Halifax</h4></div>
  <nav class="tabbar">
    <div class="tab"><svg viewBox="0 0 14 14"><path d="M2 7L7 2l5 5v6H2z" fill="none" stroke="currentColor" stroke-width="1.2"/></svg>Home</div>
    <div class="tab on"><svg viewBox="0 0 14 14"><path d="M1 5h12M1 9h12M10 2l3 3M4 12L1 9" fill="none" stroke="currentColor" stroke-width="1.2"/></svg>Exchange</div>
    <div class="tab mid"><span class="bubble"><svg viewBox="0 0 14 14"><circle cx="7" cy="7" r="5" fill="none" stroke="#fff" stroke-width="1.4"/></svg></span>Quests</div>
    <div class="tab"><svg viewBox="0 0 14 14"><circle cx="5" cy="5" r="2.5" fill="none" stroke="currentColor" stroke-width="1.2"/><path d="M1 13c0-3 2-5 4-5s4 2 4 5M9 3a2 2 0 0 1 0 4M11 9c1 1 2 2 2 4" fill="none" stroke="currentColor" stroke-width="1.2"/></svg>Partners</div>
    <div class="tab"><svg viewBox="0 0 14 14"><rect x="1" y="3" width="12" height="9" rx="2" fill="none" stroke="currentColor" stroke-width="1.2"/><path d="M9 7h4" stroke="currentColor" stroke-width="1.2"/></svg>Wallet</div>
  </nav>
</section>

<!-- Settings -->
<section class="screen" style="left:465px;top:1640px">
  <header class="header" style="height:104px;padding-top:50px">
    <h2>Settings</h2>
    <p>Change your app settings</p>
  </header>
  <div class="abs" style="left:28px;top:140px;width:160px">
    <div style="font-size:13px;font-weight:800">Sound</div>
    <div style="font-size:8px;color:var(--ink-soft);line-height:1.4;margin-top:4px">Enable the sound feature to make your experience with Tovrim more fun and exciting</div>
  </div>
  <div class="toggle" style="left:212px;top:142px;background:var(--dark-bar)"><svg width="12" height="12" viewBox="0 0 12 12"><path d="M2 4h2l3-3v10L4 8H2z" fill="none" stroke="#fff" stroke-width="1.2"/></svg></div>
  <div class="toggle" style="left:212px;top:176px;background:linear-gradient(135deg,var(--amber),var(--yellow-soft))"><svg width="12" height="12" viewBox="0 0 12 12"><path d="M2 4h2l3-3v10L4 8H2zM9 3.5c1.5 1.5 1.5 3.5 0 5" fill="none" stroke="#fff" stroke-width="1.2"/></svg></div>
  <div class="abs" style="left:28px;top:230px;width:160px">
    <div style="font-size:13px;font-weight:800">Location (GPS)</div>
    <div style="font-size:8px;color:var(--ink-soft);line-height:1.4;margin-top:4px">Enable the sound feature to make your experience with Tovrim more fun and exciting</div>
  </div>
  <div class="toggle" style="left:212px;top:232px;background:#e4e4e8"><svg width="12" height="12" viewBox="0 0 12 12"><circle cx="6" cy="6" r="3.5" fill="none" stroke="#3d3d42" stroke-width="1.2"/><path d="M6 0v2.5M6 9.5V12M0 6h2.5M9.5 6H12" stroke="#3d3d42" stroke-width="1.2"/></svg></div>
  <div class="toggle" style="left:212px;top:266px;background:linear-gradient(135deg,var(--amber),var(--yellow-soft))"><svg width="12" height="12" viewBox="0 0 12 12"><circle cx="6" cy="6" r="3.5" fill="none" stroke="#fff" stroke-width="1.2"/><circle cx="6" cy="6" r="1.2" fill="#fff"/></svg></div>
  <nav class="tabbar">
    <div class="tab"><svg viewBox="0 0 14 14"><path d="M2 7L7 2l5 5v6H2z" fill="none" stroke="currentColor" stroke-width="1.2"/></svg>Home</div>
    <div class="tab on"><svg viewBox="0 0 14 14"><path d="M1 5h12M1 9h12M10 2l3 3M4 12L1 9" fill="none" stroke="currentColor" stroke-width="1.2"/></svg>Exchange</div>
    <div class="tab mid"><span class="bubble"><svg viewBox="0 0 14 14"><circle cx="7" cy="7" r="5" fill="none" stroke="#fff" stroke-width="1.4"/></svg></span>Quests</div>
    <div class="tab"><svg viewBox="0 0 14 14"><circle cx="5" cy="5" r="2.5" fill="none" stroke="currentColor" stroke-width="1.2"/><path d="M1 13c0-3 2-5 4-5s4 2 4 5M9 3a2 2 0 0 1 0 4M11 9c1 1 2 2 2 4" fill="none" stroke="currentColor" stroke-width="1.2"/></svg>Partners</div>
    <div class="tab"><svg viewBox="0 0 14 14"><rect x="1" y="3" width="12" height="9" rx="2" fill="none" stroke="currentColor" stroke-width="1.2"/><path d="M9 7h4" stroke="currentColor" stroke-width="1.2"/></svg>Wallet</div>
  </nav>
</section>

</body>
</html>
```